Vellora Labs - Mushroom Supplement Packaging

Our brand is called Vellora Labs. I've added a couple different logos that you can use. We are creating a line up of Mushroom Supplement products. I will add the entire line-up of products here. I've added examples of other products and packaging shape types I can purchase. Give me different options for packaging that is minimalist and clean for this brand that makes it look really well made and clean and make people want to buy.

Product 1 Lions Mane 1g
Product 2 Cordyceps 1g
Product 3 Chaga 1g
Product 4 Turkey Tail 1g
Product 5 Reishi 1g
Product 6 Maitake 1g
Product 7 Shiitake 1g

Product 8 (Mix) Lions Mane 143mg
Cordyceps 143mg
Chaga 143mg
Turkey Tail 143mg
Reishi 143mg
Maitake 143mg
Shiitake 143mg

```html
<!DOCTYPE html>
<html lang="en">
<head>
<meta charset="utf-8">
<title>Vellora Labs – Shiitake Mushroom Label</title>
<link rel="stylesheet" href="https://fonts.googleapis.com/css2?family=Montserrat:wght@300;400;600;700;800&display=swap">
<style>
  :root {
    --page: #ffffff;
    --label-white: #f4f4f4;
    --label-grey: #cfcfcf;
    --peach-light: #f2c2b0;
    --peach-deep: #c9532f;
    --red-dark: #6e1214;
    --red-mid: #a3211c;
    --red-deep: #870c0c;
    --ink-dark: #2a1c16;
    --ink-mushroom: #3e0e0f;
    --text-light: #ffffff;
    --text-soft: #f1dcd6;
    --gold: #d9b54a;
  }
  * { box-sizing: border-box; margin: 0; padding: 0; }
  html, body {
    width: 1200px; height: 857px; overflow: hidden;
    background: var(--page);
    font-family: "Montserrat", sans-serif;
  }
  .canvas { position: relative; width: 1200px; height: 857px; }
  .label {
    position: absolute; left: 180px; top: 28px;
    width: 840px; height: 800px;
    overflow: hidden;
  }
  .label-art { position: absolute; inset: 0; }
  .brand {
    position: absolute; left: 0; right: 0; top: 93px;
    display: flex; align-items: center; justify-content: center; gap: 12px;
  }
  .brand-dot {
    width: 34px; height: 34px; border-radius: 50%;
    background: var(--ink-dark);
  }
  .brand-name {
    font-weight: 800; font-size: 40px; letter-spacing: 1px;
    color: var(--ink-dark); text-transform: uppercase;
  }
  .text { position: absolute; left: 0; right: 0; text-align: center; line-height: 1; }
  .product-name {
    top: 266px; font-weight: 800; font-size: 110px; letter-spacing: -1px;
    color: var(--text-light);
  }
  .product-type {
    top: 373px; font-weight: 300; font-size: 48px; letter-spacing: 3px;
    color: var(--ink-mushroom);
  }
  .support-intro {
    top: 436px; font-weight: 400; font-size: 27px; letter-spacing: 2.5px;
    color: var(--text-soft);
  }
  .benefit-pill {
    position: absolute; left: 138px; top: 477px;
    width: 572px; height: 47px; border-radius: 24px;
    background: var(--label-white);
    display: flex; align-items: center; justify-content: center;
    font-weight: 700; font-size: 26px; letter-spacing: 0.5px;
    color: var(--ink-dark);
  }
  .dose {
    position: absolute; left: 0; right: 0; top: 579px;
    display: flex; justify-content: center; align-items: baseline; gap: 10px;
    color: var(--text-light); line-height: 1;
  }
  .dose-amount { font-weight: 700; font-size: 74px; }
  .dose-unit { font-weight: 700; font-size: 38px; }
  .corner-square {
    position: absolute; left: 43px; top: 691px;
    width: 68px; height: 68px;
    border: 1.5px solid var(--text-light);
  }
  .footer {
    position: absolute; left: 0; right: 0; top: 694px;
    display: flex; justify-content: center; align-items: center; gap: 12px;
    color: var(--text-light);
  }
  .count { font-weight: 700; font-size: 28px; letter-spacing: 0.5px; }
  .divider { width: 1.5px; height: 52px; background: var(--text-light); }
  .category { font-weight: 400; font-size: 23px; line-height: 1.2; letter-spacing: 0.5px; }
</style>
</head>
<body>
<main class="canvas">
  <section class="label">
    <svg class="label-art" viewBox="0 0 840 800" width="840" height="800">
      <defs>
        <linearGradient id="redBody" x1="0" y1="0" x2="1" y2="0">
          <stop offset="0" stop-color="var(--red-dark)"/>
          <stop offset="0.5" stop-color="var(--red-mid)"/>
          <stop offset="1" stop-color="var(--red-deep)"/>
        </linearGradient>
        <linearGradient id="peachBand" x1="0" y1="0" x2="1" y2="0">
          <stop offset="0" stop-color="var(--peach-deep)"/>
          <stop offset="0.3" stop-color="var(--peach-light)"/>
          <stop offset="0.75" stop-color="var(--peach-light)"/>
          <stop offset="1" stop-color="var(--peach-deep)"/>
        </linearGradient>
        <linearGradient id="whiteBand" x1="0" y1="0" x2="1" y2="0">
          <stop offset="0" stop-color="var(--label-grey)"/>
          <stop offset="0.5" stop-color="var(--label-white)"/>
          <stop offset="1" stop-color="var(--label-grey)"/>
        </linearGradient>
      </defs>
      <rect class="red-body" role="img" aria-label="Faint line illustrations of assorted mushrooms" x="0" y="0" width="840" height="790" fill="url(#redBody)"/>
      <path class="peach-band" d="M0 0 H840 V160 C640 270 330 300 0 209 Z" fill="url(#peachBand)"/>
      <path class="white-band" d="M0 0 H840 V86 C620 230 300 250 0 25 Z" fill="url(#whiteBand)"/>
      <rect class="gold-rule" x="0" y="790" width="840" height="8" fill="var(--gold)"/>
    </svg>

    <div class="brand">
      <span class="brand-dot"></span>
      <span class="brand-name">Vellora Labs</span>
    </div>

    <h1 class="text product-name">SHIITAKE</h1>
    <p class="text product-type">MUSHROOM</p>
    <p class="text support-intro">HELPS SUPPORT</p>
    <p class="benefit-pill">CHOLESTEROL - HEART -OMMUNITY</p>

    <p class="dose"><span class="dose-amount">1000</span><span class="dose-unit">mg</span></p>

    <div class="corner-square"></div>

    <div class="footer">
      <span class="count">60 CAPSULES</span>
      <span class="divider"></span>
      <span class="category">DIETARY<br>SUPPLEMENT</span>
    </div>
  </section>
</main>
</body>
</html>
```